Sign listing benefits of Wash and Fold Service

Sign 48 inches wide and 24 inches height to showcase service listed above.
Benefits include:
Saves Money
Saves Time
Convenient
Stain Treatment

Looking for something colorful (Blue and white are our business colors) the look of a laundromat business.

```html
<!DOCTYPE html>
<html lang="en">
<head>
<meta charset="utf-8">
<title>Wash and Fold Service – Benefits Sign</title>
<link rel="stylesheet" href="https://fonts.googleapis.com/css2?family=Montserrat:wght@800&family=Poppins:wght@400&family=Barlow:wght@600&family=Barlow+Condensed:wght@700&display=swap">
<style>
  :root {
    --backdrop: #454243;
    --white: #ffffff;
    --navy: #0f2a66;
    --navy-deep: #0c2358;
    --blue-mid: #1a3c84;
    --ink: #151515;
    --icon-fill: #79b6e5;
    --icon-line: #0f2d6b;
  }
  * { margin: 0; padding: 0; box-sizing: border-box; }
  html, body { width: 1200px; height: 1200px; overflow: hidden; background: var(--backdrop); }

  .sign {
    position: absolute; left: 50px; top: 325px;
    width: 1100px; height: 550px;
    background: var(--white);
    box-shadow: 0 18px 24px rgba(0,0,0,0.35);
    overflow: hidden;
  }
  .sign__header { position: absolute; left: 0; top: 0; width: 100%; height: 168px; background: var(--white); }

  .title {
    position: absolute; left: 58px; top: 27px; width: 506px;
    font-family: "Montserrat", sans-serif; font-weight: 800;
    font-size: 62px; line-height: 1; letter-spacing: -2.5px;
    color: var(--navy); white-space: nowrap;
  }
  .subtitle {
    position: absolute; left: 57px; top: 91px; width: 504px; height: 49px;
    background: var(--ink);
    display: flex; justify-content: space-between; align-items: center;
    padding: 0 52px;
    font-family: "Poppins", sans-serif; font-weight: 400;
    font-size: 37px; color: var(--white);
  }
  .benefits-tag {
    position: absolute; left: 616px; top: 41px; width: 484px; height: 82px;
    background: var(--navy); border-radius: 8px 0 0 8px;
    display: flex; align-items: center; padding-left: 28px;
    font-family: "Barlow Condensed", sans-serif; font-weight: 700;
    font-size: 52px; letter-spacing: 2px; color: var(--white);
  }

  .sign__panel {
    position: absolute; left: 0; top: 168px; width: 100%; height: 382px;
    background: radial-gradient(ellipse at 20% 10%, var(--blue-mid) 0%, var(--navy) 55%, var(--navy-deep) 100%);
  }
  .sign__panel::after {
    content: ""; position: absolute; left: 22px; top: 0; width: 1058px; height: 359px;
    border: 1.5px solid rgba(255,255,255,0.85); border-top: none;
    border-radius: 0 0 6px 6px;
  }

  .benefit-icon { position: absolute; width: 108px; height: 108px; }
  .benefit-text {
    position: absolute;
    font-family: "Barlow", sans-serif; font-weight: 600;
    font-size: 67px; line-height: 61px; color: var(--white); white-space: nowrap;
  }
</style>
</head>
<body>
  <div class="sign">
    <header class="sign__header">
      <h1 class="title">WASH AND FOLD</h1>
      <div class="subtitle"><span>S</span><span>E</span><span>R</span><span>V</span><span>I</span><span>C</span><span>E</span></div>
      <div class="benefits-tag">BENEFITS INCLUDE:</div>
    </header>

    <section class="sign__panel">
      <!-- Saves money -->
      <svg class="benefit-icon" style="left:90px;top:46px" viewBox="0 0 100 100" aria-hidden="true">
        <circle cx="50" cy="50" r="49" fill="none" stroke="#fff" stroke-width="1.2"/>
        <circle cx="50" cy="50" r="46" fill="var(--icon-fill)"/>
        <g fill="none" stroke="var(--icon-line)" stroke-width="3.5" stroke-linecap="round" stroke-linejoin="round">
          <path d="M24 31 q10 -9 24 -7 l16 2"/>
          <rect x="66" y="22" width="5" height="11" fill="var(--icon-line)"/>
          <path d="M76 69 q-10 9 -24 7 l-16 -2"/>
          <rect x="29" y="67" width="5" height="11" fill="var(--icon-line)"/>
          <circle cx="50" cy="50" r="12"/>
        </g>
        <text x="50" y="57" text-anchor="middle" font-family="Barlow, sans-serif" font-weight="600" font-size="19" fill="var(--icon-line)">$</text>
      </svg>
      <div class="benefit-text" style="left:230px;top:35px">SAVES<br>MONEY</div>

      <!-- Convenient -->
      <svg class="benefit-icon" style="left:521px;top:41px" viewBox="0 0 100 100" aria-hidden="true">
        <circle cx="50" cy="50" r="49" fill="none" stroke="#fff" stroke-width="1.2"/>
        <circle cx="50" cy="50" r="46" fill="var(--icon-fill)"/>
        <g fill="none" stroke="var(--icon-line)" stroke-linecap="round" stroke-linejoin="round">
          <path d="M66 30 A25 25 0 1 0 72 62" stroke-width="5"/>
          <path d="M27 64 l-2 -12 10 4 z" fill="var(--icon-line)" stroke-width="2"/>
          <path d="M38 50 l10 12 22 -28" stroke-width="7"/>
        </g>
      </svg>
      <div class="benefit-text" style="left:648px;top:63px">CONVENIENT</div>

      <!-- Saves time -->
      <svg class="benefit-icon" style="left:90px;top:206px" viewBox="0 0 100 100" aria-hidden="true">
        <circle cx="50" cy="50" r="49" fill="none" stroke="#fff" stroke-width="1.2"/>
        <circle cx="50" cy="50" r="46" fill="var(--icon-fill)"/>
        <g fill="none" stroke="var(--icon-line)" stroke-linecap="round" stroke-linejoin="round">
          <circle cx="59" cy="38" r="15" stroke-width="3.5"/>
          <path d="M59 30 v8 l4 -5" stroke-width="2.5"/>
          <path d="M24 55 l8 12 q14 6 32 -2 l12 -6" stroke-width="4"/>
          <path d="M40 62 l12 -1" stroke-width="3"/>
        </g>
      </svg>
      <div class="benefit-text" style="left:230px;top:196px">SAVES<br>TIME</div>

      <!-- Stain treatment -->
      <svg class="benefit-icon" style="left:521px;top:206px" viewBox="0 0 100 100" aria-hidden="true">
        <circle cx="50" cy="50" r="49" fill="none" stroke="#fff" stroke-width="1.2"/>
        <circle cx="50" cy="50" r="46" fill="var(--icon-fill)"/>
        <g stroke="var(--icon-line)" stroke-linejoin="round">
          <path d="M38 22 q12 8 24 0 l18 9 -6 14 -8 -3 v33 h-32 v-33 l-8 3 -6 -14 z" fill="none" stroke-width="4"/>
          <path d="M28 26 q5 4 2 10 -6 2 -7 -4 z" fill="var(--icon-line)" stroke-width="1"/>
          <path d="M54 48 q6 -2 7 4 -2 6 -7 4 z" fill="none" stroke-width="2.5"/>
          <path d="M37 62 q6 4 3 10" fill="none" stroke-width="3"/>
        </g>
      </svg>
      <div class="benefit-text" style="left:655px;top:196px">STAIN<br>TREATMENT</div>
    </section>
  </div>
</body>
</html>
```